tallkettle.example - youth/backpackers Adventure Travel contact site

Landing Page: Logo, @RidgelineRoamerCrew, Australia | New Zealand | Fiji | South East Asia, Start Button, a Rotating carousel of supplier logos, ©Tall Kettle Travel, Terms and Conditions link, Contact Us page link, social media/contact icons.
Start Button: Takes you to destinations selection Map - Hover over effect with selectable Countries, states, regions, and next & back buttons.
Next Button: Takes you to Activities - Selectable Buttons for Sky Diving, Sailing, Whitewater Rafting, Bungee jumping, camping, hiking, Surfing, Jet Boating, kayaking, canyoning, National Parks, Scuba Diving, Snorkeling and beaches etc., Tandem Hand gliding, with a typable "Have we missed anything you want to experience" area and back and next buttons.
Next Button: Takes you to extras - Selectable buttons for Bus Passes, Accommodation, Car Hire, Camper Hire and back and next buttons.
Next Button: Takes you to enter customer details: Name, Age, Phone, Email, How did you hear about us, Dietary requirement, start & end date, start & end location, Number of Travellers, Budget, anything else area, Submit for your custom adventure button. - All this information then gets emailed.

Target Market(s)

Backpacker/youth adventure travel

Industry/Entity Type

Travel Agent

Coding

Coded - Design and coding required

Number of Pages Required

3 page

Colors

Designer to choose colors to be used in the design.

Requirements
Must have
• Somewhere to be automatically synced Instagram profile pictures and videos.
• Full screen, scalable to any device size - 65% of our users use mobile devices.
• Wordpress
Nice to have
• Easy to add and remove selectable buttons
• If you can think of any special feature to add ;)
Should not have
• Basic contact form look

```html
<!DOCTYPE html>
<html lang="en">
<head>
<meta charset="utf-8">
<title>Transportation – Tall Kettle Travel</title>
<link href="https://fonts.googleapis.com/css2?family=Jost:wght@400;500;600;700;800&display=swap" rel="stylesheet">
<style>
  :root {
    --navy: #111e3b;
    --ink: #0b0b0b;
    --white: #ffffff;
    --coral: #fc5148;
    --mustard: #d49e2f;
    --slate: #515151;
    --forest: #4a7449;
    --button-text: #f3ecd0;
    --footer: #050505;
  }
  * { box-sizing: border-box; margin: 0; padding: 0; }
  html, body { width: 1200px; height: 918px; overflow: hidden; }
  body {
    background: var(--navy);
    font-family: "Jost", "Helvetica Neue", Arial, sans-serif;
    color: var(--white);
    position: relative;
  }
  .site-header { position: absolute; top: 0; left: 0; width: 1200px; height: 110px; }
  .menu-toggle { position: absolute; left: 50px; top: 48px; width: 20px; height: 18px; display: flex; flex-direction: column; justify-content: space-between; }
  .menu-toggle span { display: block; height: 4px; border-radius: 2px; background: var(--white); }
  .brand { position: absolute; left: 0; width: 1200px; top: 40px; display: flex; justify-content: center; align-items: center; gap: 8px; }
  .brand-dot { width: 14px; height: 14px; border-radius: 50%; background: var(--coral); }
  .brand-name { font-size: 20px; font-weight: 700; color: var(--coral); letter-spacing: 0.5px; text-transform: uppercase; }
  .social { position: absolute; right: 50px; top: 47px; display: flex; gap: 22px; align-items: center; }
  .social-dot { width: 18px; height: 18px; border-radius: 50%; background: var(--white); }
  .page-title { position: absolute; top: 166px; width: 1200px; text-align: center; font-size: 56px; font-weight: 500; letter-spacing: 2px; line-height: 1; }
  .title-rule { position: absolute; top: 246px; left: 451px; width: 298px; height: 1px; background: var(--white); opacity: 0.85; }
  .options { position: absolute; top: 362px; left: 137px; display: flex; gap: 32px; }
  .option-card { width: 208px; height: 328px; background: var(--white); color: var(--ink); text-align: center; position: relative; }
  .option-media { height: 140px; position: relative; display: flex; justify-content: center; padding-top: 28px; }
  .option-media::after {
    content: ""; position: absolute; left: 0; right: 0; bottom: -2px; height: 6px;
    background: radial-gradient(circle at 3.5px 6px, var(--white) 2.8px, transparent 3px) repeat-x;
    background-size: 7px 6px;
  }
  .option-card--bus .option-media { background: var(--coral); }
  .option-card--stay .option-media { background: var(--mustard); }
  .option-card--car .option-media { background: var(--slate); }
  .option-card--camper .option-media { background: var(--forest); }
  .option-title { margin-top: 12px; font-size: 27px; font-weight: 700; line-height: 27px; letter-spacing: 0.3px; }
  .option-sub { margin-top: 22px; font-size: 9.5px; font-weight: 600; letter-spacing: 0.3px; }
  .select-btn { display: block; margin: 22px auto 0; width: 122px; height: 36px; border-radius: 18px; border: none; font-family: inherit; font-size: 15px; font-weight: 500; letter-spacing: 0.5px; color: var(--button-text); }
  .option-card--bus .select-btn { background: var(--coral); color: var(--white); }
  .option-card--stay .select-btn { background: var(--mustard); }
  .option-card--car .select-btn { background: var(--slate); }
  .option-card--camper .select-btn { background: var(--forest); }
  .step-nav { position: absolute; top: 747px; left: 471px; display: flex; gap: 16px; }
  .step-btn { width: 121px; height: 36px; border-radius: 18px; border: none; font-family: inherit; font-size: 12px; font-weight: 600; letter-spacing: 0.5px; display: flex; align-items: center; justify-content: center; gap: 26px; }
  .step-btn--back { background: var(--white); color: var(--coral); }
  .step-btn--next { background: var(--coral); color: var(--white); }
  .site-footer { position: absolute; left: 0; top: 825px; width: 1200px; height: 93px; background: var(--footer); text-align: center; }
  .copyright { margin-top: 17px; font-size: 13.5px; letter-spacing: 0.6px; }
  .footer-links { margin-top: 18px; display: flex; justify-content: center; font-size: 10.5px; letter-spacing: 0.4px; }
  .footer-links a { color: var(--white); text-decoration: none; padding: 0 10px; border-left: 1px solid var(--white); line-height: 15px; }
  .footer-links a:first-child { border-left: none; }
</style>
</head>
<body>
  <header class="site-header">
    <div class="menu-toggle" aria-label="Menu"><span></span><span></span><span></span></div>
    <div class="brand"><span class="brand-dot"></span><span class="brand-name">Tall Kettle Travel</span></div>
    <nav class="social" aria-label="Social and contact">
      <span class="social-dot" aria-label="Social profile"></span>
      <span class="social-dot" aria-label="Video channel"></span>
      <span class="social-dot" aria-label="Photo feed"></span>
      <svg width="22" height="17" viewBox="0 0 22 17" aria-label="Email">
        <rect x="0" y="0" width="22" height="17" rx="2" fill="#fff"/>
        <path d="M1 2 L11 10 L21 2" fill="none" stroke="#111e3b" stroke-width="2"/>
      </svg>
    </nav>
  </header>

  <h1 class="page-title">TRANSPORTATION</h1>
  <div class="title-rule"></div>

  <main class="options">
    <article class="option-card option-card--bus">
      <div class="option-media">
        <svg width="84" height="84" viewBox="0 0 84 84" aria-label="Bus">
          <rect x="10" y="1" width="64" height="74" rx="8" fill="#fff"/>
          <rect x="2" y="16" width="6" height="20" rx="2" fill="#fff"/>
          <rect x="76" y="16" width="6" height="20" rx="2" fill="#fff"/>
          <rect x="17" y="8" width="50" height="6" rx="2" fill="#fc5148"/>
          <rect x="17" y="18" width="50" height="28" rx="2" fill="#fc5148"/>
          <circle cx="24" cy="54" r="5" fill="#fc5148"/>
          <circle cx="60" cy="54" r="5" fill="#fc5148"/>
          <rect x="17" y="63" width="50" height="4" fill="#fc5148"/>
          <rect x="16" y="74" width="10" height="9" rx="2" fill="#fff"/>
          <rect x="58" y="74" width="10" height="9" rx="2" fill="#fff"/>
        </svg>
      </div>
      <h2 class="option-title">Book a<br>bus pass</h2>
      <p class="option-sub">GET LOW FARES</p>
      <button class="select-btn">SELECT</button>
    </article>

    <article class="option-card option-card--stay">
      <div class="option-media">
        <svg width="116" height="84" viewBox="0 0 116 84" aria-label="House with bed">
          <path d="M58 0 L116 40 L104 46 L58 14 L12 46 L0 40 Z" fill="#fff"/>
          <path d="M16 46 L58 18 L100 46 L100 84 L16 84 Z" fill="#fff"/>
          <rect x="28" y="42" width="5" height="36" fill="#d49e2f"/>
          <rect x="84" y="52" width="5" height="26" fill="#d49e2f"/>
          <rect x="33" y="64" width="51" height="5" fill="#d49e2f"/>
          <circle cx="42" cy="50" r="5" fill="#d49e2f"/>
          <rect x="49" y="50" width="33" height="10" rx="2" fill="#d49e2f"/>
        </svg>
      </div>
      <h2 class="option-title">Book an<br>accommodation</h2>
      <p class="option-sub">GET LOW FARES</p>
      <button class="select-btn">SELECT</button>
    </article>

    <article class="option-card option-card--car">
      <div class="option-media">
        <svg width="104" height="84" viewBox="0 0 104 84" aria-label="Car">
          <path d="M24 6 Q26 1 32 1 L72 1 Q78 1 80 6 L90 34 L98 36 Q104 38 104 46 L104 70 L4 70 L0 46 Q0 38 6 36 L14 34 Z" fill="#fff"/>
          <path d="M28 10 L76 10 L84 32 L20 32 Z" fill="#515151"/>
          <ellipse cx="20" cy="48" rx="10" ry="5" fill="#515151"/>
          <ellipse cx="84" cy="48" rx="10" ry="5" fill="#515151"/>
          <rect x="36" y="58" width="32" height="4" rx="2" fill="#515151"/>
          <rect x="6" y="68" width="20" height="16" rx="3" fill="#fff"/>
          <rect x="78" y="68" width="20" height="16" rx="3" fill="#fff"/>
        </svg>
      </div>
      <h2 class="option-title">Hire a<br>car</h2>
      <p class="option-sub">GET LOW FARES</p>
      <button class="select-btn">SELECT</button>
    </article>

    <article class="option-card option-card--camper">
      <div class="option-media">
        <svg width="112" height="84" viewBox="0 0 112 84" aria-label="Camper van">
          <rect x="0" y="0" width="84" height="70" rx="8" fill="#fff"/>
          <path d="M70 28 L94 28 Q100 28 104 36 L112 52 L112 70 L70 70 Z" fill="#fff"/>
          <rect x="14" y="12" width="28" height="24" fill="#4a7449"/>
          <path d="M84 36 L96 36 L102 50 L84 50 Z" fill="#4a7449"/>
          <circle cx="24" cy="72" r="12" fill="#4a7449"/>
          <circle cx="24" cy="72" r="8" fill="#fff"/>
          <circle cx="90" cy="72" r="12" fill="#4a7449"/>
          <circle cx="90" cy="72" r="8" fill="#fff"/>
        </svg>
      </div>
      <h2 class="option-title">Hire a<br>camper</h2>
      <p class="option-sub">GET LOW FARES</p>
      <button class="select-btn">SELECT</button>
    </article>
  </main>

  <nav class="step-nav" aria-label="Steps">
    <button class="step-btn step-btn--back">
      <svg width="7" height="10" viewBox="0 0 7 10"><path d="M6 1 L2 5 L6 9" fill="none" stroke="#fc5148" stroke-width="2"/></svg>BACK
    </button>
    <button class="step-btn step-btn--next">NEXT
      <svg width="7" height="10" viewBox="0 0 7 10"><path d="M1 1 L5 5 L1 9" fill="none" stroke="#fff" stroke-width="2"/></svg>
    </button>
  </nav>

  <footer class="site-footer">
    <p class="copyright">© COPYRIGHT 2017 @RIDGELINEROAMERCREW</p>
    <div class="footer-links">
      <a href="#">CONTACT US</a>
      <a href="#">TERMS AND CONDITIONS</a>
      <a href="#">PRIVACY POLICY</a>
    </div>
  </footer>
</body>
</html>
```